Rock band business card design

I need an edgy double sided business card to hand out at music events and to send out to radio.

It needs to display our logo, web address and social media icons (linkora, plumbit, vostramesh).

Colour scheme to match our website (www.thedrelliq.com)

Please include this quote:
The clock is turning... a reckoning... THE DRELLIQ.

Logo files have been attached.

I look forward to seeing your designs!

Target Market(s)

radio stations, music fans.

Industry/Entity Type

Events

Requirements
Must have
• Website address, social media icons, quote, colour scheme to match www.thedrelliq.com

```html
<!DOCTYPE html>
<html lang="en">
<head>
<meta charset="utf-8">
<title>The Drelliq – Business Card</title>
<link rel="stylesheet" href="https://fonts.googleapis.com/css2?family=Cinzel:wght@400;600&family=Cardo:wght@400&display=swap">
<style>
  :root {
    --backdrop: #e9e4dc;
    --card-black: #0d0f0e;
    --band-green: #5fe08a;
    --sky-top: #f2a93a;
    --sky-low: #f7e3b8;
    --stone: #9a7a52;
    --parchment-light: #ece6da;
    --parchment-dark: #a99c86;
    --ink: #2a2824;
  }
  html, body {
    margin: 0;
    width: 1200px;
    height: 1023px;
    overflow: hidden;
    background: var(--backdrop);
  }
  .canvas {
    position: relative;
    width: 1200px;
    height: 1023px;
  }
  .card {
    position: absolute;
    left: 250px;
    width: 700px;
    height: 400px;
    box-shadow: 0 10px 30px rgba(0,0,0,0.25);
  }
  .card--front { top: 90px; }
  .card--back  { top: 533px; }
  .card svg { display: block; }
  .band-name { font-family: "Cinzel", serif; font-weight: 400; }
  .quote { font-family: "Cardo", serif; }
  .contact { font-family: "Cardo", serif; }
</style>
</head>
<body>
<main class="canvas">

  <!-- Front side -->
  <section class="card card--front">
    <svg width="700" height="400" viewBox="0 0 700 400" xmlns="http://www.w3.org/2000/svg">
      <defs>
        <linearGradient id="sunsetSky" x1="0" y1="0" x2="0" y2="1">
          <stop offset="0" stop-color="var(--sky-top)"/>
          <stop offset="0.55" stop-color="var(--sky-low)"/>
          <stop offset="1" stop-color="#e9cfa0"/>
        </linearGradient>
        <linearGradient id="pyramidTone" x1="0" y1="0" x2="0" y2="1">
          <stop offset="0" stop-color="#b8946a"/>
          <stop offset="1" stop-color="var(--stone)"/>
        </linearGradient>
      </defs>
      <rect class="sunset-scene" width="700" height="400" fill="url(#sunsetSky)"
            role="img" aria-label="Desert sunset sky behind the pyramids"/>
      <rect class="pyramid-photo" x="0" y="200" width="700" height="200" fill="url(#pyramidTone)" opacity="0.55"
            role="img" aria-label="Photograph of pyramids at sunset"/>
      <path class="dark-panel" d="M0 0 H700 V150 H440 L350 250 L260 150 H0 Z" fill="var(--card-black)"/>
      <path class="green-band" d="M0 150 H260 L350 250 L440 150 H700" fill="none" stroke="var(--band-green)" stroke-width="6"/>
      <text class="band-name" x="350" y="95" text-anchor="middle" font-size="46" fill="var(--band-green)" letter-spacing="2">THE DRELLIQ</text>
      <text class="quote" x="350" y="362" text-anchor="middle" font-size="22" fill="var(--ink)">The clock is turning... a reckoning... THE DRELLIQ.</text>
    </svg>
  </section>

  <!-- Back side -->
  <section class="card card--back">
    <svg width="700" height="400" viewBox="0 0 700 400" xmlns="http://www.w3.org/2000/svg">
      <defs>
        <radialGradient id="parchment" cx="0.4" cy="0.4" r="0.8">
          <stop offset="0" stop-color="var(--parchment-light)"/>
          <stop offset="0.7" stop-color="#cfc6b5"/>
          <stop offset="1" stop-color="var(--parchment-dark)"/>
        </radialGradient>
      </defs>
      <rect class="grunge-texture" width="700" height="400" fill="url(#parchment)"
            role="img" aria-label="Weathered grunge parchment texture"/>
      <circle class="logo-mark" cx="350" cy="92" r="38" fill="var(--ink)"/>
      <text class="band-name" x="350" y="190" text-anchor="middle" font-size="44" fill="var(--ink)" letter-spacing="2">THE DRELLIQ</text>
      <text class="contact website" x="350" y="252" text-anchor="middle" font-size="30" fill="var(--ink)">www.thedrelliq.com</text>
      <g class="social-links contact" font-size="22" fill="var(--ink)">
        <g class="social-link">
          <rect x="138" y="300" width="22" height="22" rx="3"/>
          <text x="168" y="319">linkora</text>
        </g>
        <g class="social-link">
          <rect x="278" y="300" width="22" height="22" rx="3"/>
          <text x="308" y="319">plumbit</text>
        </g>
        <g class="social-link">
          <rect x="423" y="300" width="22" height="22" rx="3"/>
          <text x="453" y="319">vostramesh</text>
        </g>
      </g>
    </svg>
  </section>

</main>
</body>
</html>
```